Graphic design for Student Conference

We need design work done for our annual student conference called Lantern Fest. We have a central logo but need design work done to use on posters, banners, etc. that tie into the theme for this year's conference. The theme is "Be Glad" and I would like the design elements to have a very fun, 1980's or 1990's vibe to them. The feeling of happiness and joy should be felt in the design.

Target Market(s)

Students 10-12 years of age

Industry/Entity Type

Church

Requirements
Must have
• Must include the Lantern Fest logo - event date: June 19-21 - event website: brightoakparish.org/lanternfest - Flexible supporting artwork elements that can be used in a variety of mediums. - Must use fonts that are available from free, open sources or can be provided upon delivery of completed project.
Should not have
• Anything crude, scary or content inappropriate for middle school students. Should not have any imagery related to a classroom or meeting.

```html
<!DOCTYPE html>
<html lang="en">
<head>
<meta charset="utf-8">
<title>Lantern Fest 2022 Poster</title>
<link rel="stylesheet" href="https://fonts.googleapis.com/css2?family=Passion+One:wght@700&family=Titan+One&family=Montserrat:wght@900&family=Archivo+Black&display=swap">
<style>
  :root {
    --page: #ffffff;
    --ink: #000000;
    --sun: #fdea2b;
    --magenta: #be0099;
    --sky: #1e9bd7;
    --lime: #9be81a;
    --violet: #7a4fc0;
    --paper: #ffffff;
  }
  html, body {
    margin: 0;
    width: 1200px;
    height: 1200px;
    overflow: hidden;
    background: var(--page);
  }
  .canvas {
    position: relative;
    width: 1200px;
    height: 1200px;
  }
  .poster {
    position: absolute;
    left: 253px;
    top: 80px;
    width: 694px;
    height: 1040px;
    display: block;
  }
  .date-days {
    font-family: "Passion One", sans-serif;
    font-weight: 700;
    font-size: 54px;
    fill: var(--sky);
  }
  .date-year {
    font-family: "Titan One", sans-serif;
    font-size: 112px;
    fill: var(--sun);
  }
  .event-name {
    font-family: "Montserrat", sans-serif;
    font-weight: 900;
    font-size: 44px;
    fill: var(--sun);
  }
  .event-url {
    font-family: "Archivo Black", sans-serif;
    font-size: 13.5px;
    letter-spacing: 2.4px;
    fill: var(--paper);
  }
</style>
</head>
<body>
<main class="canvas">
  <svg class="poster" viewBox="0 0 867 1300" xmlns="http://www.w3.org/2000/svg" aria-label="Lantern Fest 2022 poster">
    <defs>
      <clipPath id="poster-bounds">
        <rect width="867" height="1300"/>
      </clipPath>
      <linearGradient id="stripe-gradient" x1="0" y1="0" x2="0.6" y2="1">
        <stop offset="0" stop-color="var(--lime)"/>
        <stop offset="0.5" stop-color="var(--sky)"/>
        <stop offset="0.78" stop-color="var(--violet)"/>
        <stop offset="1" stop-color="var(--magenta)"/>
      </linearGradient>
      <path id="stripe-path" d="M-10 215 L660 1010 Q690 1048 676 1080 L590 1320"/>
    </defs>

    <g clip-path="url(#poster-bounds)">
      <rect class="poster-ground" width="867" height="1300" fill="var(--paper)"/>
      <polygon class="night-panel" points="0,270 660,1050 575,1300 0,1300" fill="var(--ink)"/>

      <circle class="sun-artwork" cx="555" cy="460" r="462" fill="var(--sun)"
              role="img" aria-label="Large yellow sun character artwork"/>

      <g class="rainbow-stripes" fill="none">
        <use href="#stripe-path" stroke="url(#stripe-gradient)" stroke-width="10"/>
        <use href="#stripe-path" transform="translate(-8 14)" stroke="var(--paper)" stroke-width="4"/>
        <use href="#stripe-path" transform="translate(-16 26)" stroke="var(--ink)" stroke-width="4"/>
        <use href="#stripe-path" transform="translate(-24 38)" stroke="url(#stripe-gradient)" stroke-width="9"/>
        <use href="#stripe-path" transform="translate(-34 50)" stroke="var(--ink)" stroke-width="5"/>
      </g>

      <text class="date-days" x="220" y="965" text-anchor="middle">JUNE 19-21</text>
      <text class="date-year" x="220" y="1068" text-anchor="middle">2022</text>
      <text class="event-name" x="220" y="1168" text-anchor="middle">LANTERN FEST</text>
      <text class="event-url" x="33" y="1270">WWW.BRIGHTOAKPARISH.ORG/LANTERNFEST</text>
    </g>
  </svg>
</main>
</body>
</html>
```